KL Taxidermy

I need business Cards with my logo and a background photo of one of my taxidermy mounts.
I would like a black back drop behind it all and what ever looks best for my contact information (red or white?)
Garrick Pembley
592-718-4409
kltaxidermy482@mailnook.example
Chatterloom page

```html
<!DOCTYPE html>
<html lang="en">
<head>
<meta charset="utf-8">
<title>KL Taxidermy — Business Card</title>
<link href="https://fonts.googleapis.com/css2?family=Montserrat:wght@400;500;600&display=swap" rel="stylesheet">
<style>
  :root {
    --page-bg: #e9e9e7;
    --card-light: #3d4143;
    --card-dark: #1b1d1e;
    --text-light: #f1f1ef;
    --accent-copper: #c98650;
    --mount-white: #d8d8d2;
    --mount-rock: #4a5158;
  }
  * { box-sizing: border-box; margin: 0; padding: 0; }
  html, body { width: 1200px; height: 900px; overflow: hidden; }
  body {
    background: var(--page-bg);
    font-family: "Montserrat", sans-serif;
    display: flex; align-items: center; justify-content: center;
  }
  .business-card {
    position: relative;
    width: 1050px; height: 600px;
    background: radial-gradient(ellipse at 45% 35%, var(--card-light) 0%, #2a2d2f 55%, var(--card-dark) 100%);
    box-shadow: 0 10px 30px rgba(0,0,0,0.25);
    overflow: hidden;
    color: var(--text-light);
  }
  .brand-mark {
    position: absolute; left: 150px; top: 80px;
    display: flex; align-items: center; gap: 14px;
  }
  .brand-square { width: 26px; height: 26px; background: var(--text-light); }
  .brand-name {
    font-size: 32px; font-weight: 600; letter-spacing: 2px;
    text-transform: uppercase; color: var(--text-light);
  }
  .contact-list {
    position: absolute; left: 150px; top: 250px;
    list-style: none; font-size: 22px; font-weight: 400;
  }
  .contact-list li { display: flex; align-items: center; gap: 18px; height: 42px; white-space: nowrap; }
  .contact-icon { width: 22px; height: 22px; flex: none; }
  .mailing-address {
    position: absolute; left: 150px; top: 390px;
    font-size: 22px; line-height: 42px; font-style: normal; white-space: nowrap;
  }
  .mount-photo {
    position: absolute; left: 640px; top: 290px;
    width: 360px; height: 310px;
    background:
      radial-gradient(ellipse 55% 38% at 55% 35%, var(--mount-white) 0%, rgba(216,216,210,0.55) 55%, transparent 78%),
      linear-gradient(180deg, transparent 50%, var(--mount-rock) 72%, #2f353a 100%);
    border-radius: 40% 30% 8% 20%;
  }
  .owner {
    position: absolute; left: 700px; top: 175px;
    white-space: nowrap;
  }
  .owner-name { font-size: 34px; font-weight: 600; color: var(--accent-copper); line-height: 1.15; }
  .owner-title { font-size: 30px; font-weight: 400; color: var(--text-light); line-height: 1.2; }
</style>
</head>
<body>
  <section class="business-card">
    <div class="brand-mark">
      <span class="brand-square"></span>
      <span class="brand-name">KL Taxidermy</span>
    </div>

    <ul class="contact-list">
      <li>
        <svg class="contact-icon" viewBox="0 0 24 24"><path fill="var(--accent-copper)" d="M6.6 2.5l3 3.4-2 2.3c1.2 2.8 3.4 5 6.2 6.2l2.3-2 3.4 3-1.8 3.8C10 19.1 4.9 14 4.6 4.3z"/></svg>
        <span>592-718-4409</span>
      </li>
      <li>
        <svg class="contact-icon" viewBox="0 0 24 24"><rect x="2" y="5" width="20" height="14" fill="var(--accent-copper)"/><path d="M2 5l10 8 10-8" stroke="#2a2d2f" stroke-width="1.6" fill="none"/></svg>
        <span>kltaxidermy482@mailnook.example</span>
      </li>
      <li>
        <svg class="contact-icon" viewBox="0 0 24 24"><rect x="2" y="2" width="20" height="20" rx="2" fill="var(--accent-copper)"/></svg>
        <span>KL Taxidermy</span>
      </li>
    </ul>

    <address class="mailing-address">
      Garrick Pembley, Caja 41736<br>
      Larchmere, YT, X0B 3K7
    </address>

    <div class="mount-photo" role="img" aria-label="Photo of a white Dall sheep ram mount lying on a grey rock base"></div>

    <div class="owner">
      <p class="owner-name">Garrick Pembley</p>
      <p class="owner-title">Taxidermist</p>
    </div>
  </section>
</body>
</html>
```